Personal wordpress site

I am documenting a few changes in my life and am looking for a designed wordpress theme to upload photos and short videos and a blurb tha tI can submit that will document the changes on a daily basis (for 12 weeks). It is a relatively straightforward site but one where I would like to track multiple projects in succession and have all the information.

• I am looking for a dark, clean design.

```html
<!DOCTYPE html>
<html lang="en">
<head>
<meta charset="utf-8">
<title>Mark Ellison</title>
<link href="https://fonts.googleapis.com/css2?family=Poiret+One&family=Open+Sans:wght@400;600&display=swap" rel="stylesheet">
<style>
:root{
  --ink:#2b2b2b;
  --text:#555;
  --muted:#777;
  --nav-top:#5a5a5a;
  --nav-bottom:#2e2e2e;
  --nav-active:#1f1f1f;
  --panel:rgba(70,70,70,.88);
  --soft:#e9e9e9;
  --line:#dcdcdc;
  --footer:#3a3a3a;
  --footer-text:#cfcfcf;
  --white:#fff;
}
*{box-sizing:border-box;margin:0;padding:0}
html,body{width:758px;height:1200px;overflow:hidden;background:var(--white)}
body{position:relative;font-family:"Open Sans",Arial,sans-serif;color:var(--text)}
.abs{position:absolute}
.display{font-family:"Poiret One","Century Gothic",sans-serif;color:var(--ink);font-weight:400}

.site-title{left:62px;top:8px;font-size:38px;letter-spacing:.5px}
.search{left:562px;top:18px;width:133px;height:22px;border:1px solid #cfcfcf;font-size:8.5px;color:#888;padding:5px 8px}
.search svg{position:absolute;right:6px;top:5px}

.nav{left:0;top:60px;width:758px;height:33px;background:linear-gradient(var(--nav-top),var(--nav-bottom));border-top:1px solid #888}
.nav-item{position:absolute;top:0;height:32px;line-height:32px;text-align:center;color:#eee;font-size:10px;text-transform:uppercase;border-right:1px solid #222;box-shadow:1px 0 0 #5e5e5e}
.nav-item.active{background:var(--nav-active)}
.nav-edge{position:absolute;left:63px;top:0;width:1px;height:32px;background:#222}

.hero{left:62px;top:102px;width:634px;height:272px;background:linear-gradient(90deg,#1d1f14 0%,#3c4a25 25%,#6b5a3c 45%,#4a4030 60%,#2a2a28 75%,#141414 100%)}
.hero-panel{left:76px;top:116px;width:180px;height:243px;background:var(--panel)}
.book-cover{left:93px;top:130px;width:57px;height:74px;border-radius:5px;background:linear-gradient(#2a0f2a,#8a2a5a 60%,#1a3a6a);border:2px solid #222}
.hero-title{left:163px;top:142px;width:90px;color:var(--white);font-size:12.5px;font-weight:600;line-height:17.5px}
.hero-copy{left:90px;top:212px;width:160px;color:#ddd;font-size:9px;line-height:16px}
.buy-btn{left:90px;top:270px;width:150px;height:27px;background:linear-gradient(#fff,#e4e4e4);border:1px solid #bbb;border-radius:2px;color:#333;font-size:11.5px;line-height:25px;padding-left:42px}
.buy-btn svg{position:absolute;left:16px;top:6px}
.dot{top:328px;width:9px;height:9px;border-radius:50%;background:#999}
.dot.on{background:#555;box-shadow:inset 0 1px 1px #222}

.section-title{font-size:24px}
.copy{font-size:8.4px;line-height:14.4px}
.rule{height:1px;background:var(--line)}

.arrow-btn{top:552px;width:13px;height:13px;border-radius:50%;background:#ddd;border:1px solid #ccc}
.arrow-btn svg{position:absolute;left:3px;top:3px}

.card{top:582px;width:140px;height:176px;background:var(--soft);border:1px solid #d5d5d5}
.card-photo{position:absolute;left:2px;top:2px;width:134px;height:89px}
.card-title{position:absolute;left:7px;top:101px;font-size:9.3px;font-weight:600;color:#222}
.card-date{position:absolute;left:7px;top:114px;font-size:7.5px;color:#333}
.card-text{position:absolute;left:7px;top:131px;width:122px;font-size:7.4px;line-height:12px;color:var(--muted)}

.categories{left:527px;top:427px;width:168px;height:217px;background:var(--soft)}
.cat{position:absolute;left:23px;font-size:9.6px;color:var(--muted)}
.cat::before{content:"";position:absolute;left:-13px;top:4px;border-left:4px solid #888;border-top:3px solid transparent;border-bottom:3px solid transparent}

.video{left:527px;top:654px;width:168px;height:104px;background:linear-gradient(90deg,#141414,#2a2a2a 60%,#3a3a3a)}

.blog-box{left:63px;top:826px;width:632px;height:127px;border:1px solid #ddd;background:linear-gradient(#fff 60%,#f3f3f3)}
.blog-photo{left:71px;top:834px;width:169px;height:111px;background:linear-gradient(135deg,#0e0e12,#2a2a33 50%,#7a5a48 75%,#222)}
.blog-title{left:254px;top:834px;font-size:10px;font-weight:600;color:#111}
.blog-date{left:254px;top:848px;font-size:7.5px;color:#333}
.blog-copy{left:254px;top:864px;width:420px;font-size:8.2px;line-height:13.2px}
.share{top:929px;height:13px;font-size:7px;line-height:11px;border:1px solid #c8c8c8;border-radius:2px;padding:0 4px;background:linear-gradient(#fff,#eee);color:#333}
.share .sq{display:inline-block;width:6px;height:6px;background:#888;margin-right:3px;vertical-align:-0.5px}
.share.count{color:#555}
.share.hot{background:#e8553e;border-color:#c9432f;color:var(--white)}
.share.hot .sq{background:var(--white)}

.gallery-photo{top:1022px;width:145px;height:92px}

.footer{left:0;top:1134px;width:758px;height:66px;background:var(--footer)}
.footer-links{left:63px;top:1148px;font-size:8.3px;color:var(--footer-text);word-spacing:1px}
.footer-links span{margin:0 5px;color:#999}
.copyright{left:63px;top:1171px;font-size:8.3px;color:var(--footer-text)}
.social{top:1159px;width:16px;height:16px;border-radius:50%;background:#666}
</style>
</head>
<body>

<header>
  <div class="abs display site-title">Mark Ellison</div>
  <div class="abs search">Search
    <svg width="10" height="10" viewBox="0 0 10 10"><circle cx="4" cy="4" r="3" fill="none" stroke="#222" stroke-width="1.6"/><line x1="6" y1="6" x2="9.5" y2="9.5" stroke="#222" stroke-width="2"/></svg>
  </div>
  <nav class="abs nav">
    <span class="nav-edge"></span>
    <a class="nav-item active" style="left:63px;width:90px">Home</a>
    <a class="nav-item" style="left:153px;width:114px">About Me</a>
    <a class="nav-item" style="left:267px;width:112px">Publishes</a>
    <a class="nav-item" style="left:379px;width:107px">In Media</a>
    <a class="nav-item" style="left:486px;width:89px">Blog</a>
    <a class="nav-item" style="left:575px;width:120px">Contact Me</a>
  </nav>
</header>

<section>
  <div class="abs hero" role="img" aria-label="Portrait of the author in a tweed jacket on a tree-lined path"></div>
  <div class="abs hero-panel"></div>
  <div class="abs book-cover" role="img" aria-label="Book cover shown on a tablet"></div>
  <div class="abs hero-title">Aliquam pellentesque lacinia dolor.</div>
  <p class="abs hero-copy">Pellentesque et semper mi. Integer tincidunt sit amet sem et rhoncus. Nulla nisl orci, tristique et urna.</p>
  <div class="abs buy-btn">
    <svg width="18" height="14" viewBox="0 0 18 14"><path d="M1 1h3l2 8h9l2-6H5" fill="none" stroke="#333" stroke-width="1.4"/><circle cx="7" cy="12" r="1.3" fill="#333"/><circle cx="14" cy="12" r="1.3" fill="#333"/></svg>
    BUY THIS BOOK
  </div>
  <span class="abs dot on" style="left:146px"></span>
  <span class="abs dot" style="left:161px"></span>
  <span class="abs dot" style="left:176px"></span>
  <span class="abs dot" style="left:191px"></span>
</section>

<main>
  <h2 class="abs display section-title" style="left:62px;top:392px">Welcome</h2>
  <p class="abs copy" style="left:63px;top:424px;width:446px">Sed pellentesque nibh non orci aliquet tempus non id orci. Duis dapibus in nisl ac aliquet. Aliquam ac interdum arcu, vitae vestibulum mi. Maecenas varius nisl at sodales fermentum. Ut non quam aliquam, luctus diam eget, congue justo. Duis tempor eget erat ut malesuada. Suspendisse pulvinar nunc velit, non auctor elit feugiat at. Praesent molestie lorem ac lacinia fermentum. Nullam elit lorem, mattis ac justo vel.</p>
  <p class="abs copy" style="left:63px;top:487px;width:446px">Nulla accumsan mi arcu, ut tempus nibh porttitor sit amet. Nunc ullamcorper elit vel nibh sagittis, eget dictum nisi adipiscing. Integer ultrices, lacus non auctor dictum, velit lacus feugiat ante.</p>
  <div class="abs rule" style="left:63px;top:528px;width:451px"></div>

  <h2 class="abs display section-title" style="left:62px;top:547px">My Publishes</h2>
  <span class="abs arrow-btn" style="left:486px"><svg width="7" height="7" viewBox="0 0 7 7"><path d="M4.5 1L2 3.5 4.5 6" fill="none" stroke="#555" stroke-width="1.2"/></svg></span>
  <span class="abs arrow-btn" style="left:501px"><svg width="7" height="7" viewBox="0 0 7 7"><path d="M2.5 1L5 3.5 2.5 6" fill="none" stroke="#555" stroke-width="1.2"/></svg></span>

  <article class="abs card" style="left:63px">
    <div class="card-photo" role="img" aria-label="Silhouette of a horse against a pink evening sky" style="background:linear-gradient(135deg,#3a2a3a,#b87a8a 45%,#2a1a22)"></div>
    <div class="card-title">Aliquam ac interdum arcu</div>
    <div class="card-date">January 11, 2013</div>
    <p class="card-text">Praesent molestie lorem ac lacinia fermentum. Nullam elit lorem, mattis ac justo vel.</p>
  </article>
  <article class="abs card" style="left:219px">
    <div class="card-photo" role="img" aria-label="Man leaping across a gap in a broken bridge" style="background:linear-gradient(#b8c4d0,#dfe4ea 45%,#6a6e72)"></div>
    <div class="card-title">Aliquam ac interdum arcu</div>
    <div class="card-date">January 11, 2013</div>
    <p class="card-text">Praesent molestie lorem ac lacinia fermentum. Nullam elit lorem, mattis ac justo vel.</p>
  </article>
  <article class="abs card" style="left:374px">
    <div class="card-photo" role="img" aria-label="Man running across snow carrying a paper plane" style="background:linear-gradient(#c8d2dc,#eef0f2 55%,#f6f6f6)"></div>
    <div class="card-title">Aliquam ac interdum arcu</div>
    <div class="card-date">January 11, 2013</div>
    <p class="card-text">Praesent molestie lorem ac lacinia fermentum. Nullam elit lorem, mattis ac justo vel.</p>
  </article>

  <aside>
    <h2 class="abs display section-title" style="left:527px;top:394px">Categories</h2>
    <ul class="abs categories" style="list-style:none">
      <li class="cat" style="top:13px">Nunc venenatis</li>
      <li class="cat" style="top:35px">Aliquam dolor dolor</li>
      <li class="cat" style="top:58px">Aliquam pellentesque</li>
      <li class="cat" style="top:80px">Proin mattis</li>
      <li class="cat" style="top:103px">Proin mattis</li>
      <li class="cat" style="top:125px">Praesent molestie lorem</li>
      <li class="cat" style="top:148px">Aenean lacinia</li>
      <li class="cat" style="top:170px">Duis tempor eget</li>
      <li class="cat" style="top:192px">Aenean ut</li>
    </ul>
    <div class="abs video" role="img" aria-label="Video still of the author in a suit"></div>
    <svg class="abs" style="left:591px;top:686px" width="40" height="40" viewBox="0 0 40 40"><circle cx="20" cy="20" r="18" fill="rgba(0,0,0,.25)" stroke="#fff" stroke-width="2.5"/><path d="M15 11l13 9-13 9z" fill="#fff"/></svg>
  </aside>

  <div class="abs rule" style="left:63px;top:778px;width:632px"></div>

  <h2 class="abs display section-title" style="left:62px;top:791px">Blog</h2>
  <article>
    <div class="abs blog-box"></div>
    <div class="abs blog-photo" role="img" aria-label="Close-up of a man adjusting his tie"></div>
    <div class="abs blog-title">Sed tincidunt nibh magna, ut posuere mauris consequat vitae</div>
    <div class="abs blog-date">January 11, 2013</div>
    <p class="abs blog-copy">Aliquam ultrices dui ut ligula vestibulum elementum. Vestibulum suscipit dui nisi, quis consequat nibh gravida quis. Proin mattis, quam quis tincidunt condimentum, ligula enim venenatis lacus, vel commodo augue mauris id sem. Vestibulum id ante ornare, congue odio ut, imperdiet lorem. Cum sociis natoque penatibus et magnis dis parturient montes, nascetur ridiculus mus.</p>
    <span class="abs share" style="left:254px"><i class="sq"></i>Like</span>
    <span class="abs share count" style="left:288px">3k</span>
    <span class="abs share" style="left:308px"><i class="sq"></i>Post</span>
    <span class="abs share count" style="left:349px">316</span>
    <span class="abs share" style="left:374px"><i class="sq"></i>+1</span>
    <span class="abs share count" style="left:400px">81</span>
    <span class="abs share hot" style="left:424px"><i class="sq"></i>Share</span>
    <span class="abs share count" style="left:462px">4.6K</span>
  </article>

  <div class="abs rule" style="left:63px;top:970px;width:632px"></div>

  <h2 class="abs display section-title" style="left:62px;top:988px">Gallery</h2>
  <div class="abs gallery-photo" style="left:63px;background:linear-gradient(90deg,#111,#3a3a44 50%,#111)" role="img" aria-label="Man in an argyle sweater standing between two lights at night"></div>
  <div class="abs gallery-photo" style="left:226px;background:linear-gradient(#8a8a8a,#d4d4d4 55%,#9a9a9a)" role="img" aria-label="Open book lying on a grey surface"></div>
  <div class="abs gallery-photo" style="left:388px;background:linear-gradient(90deg,#4a4448,#b08a78 50%,#4a4448)" role="img" aria-label="Laced corset seen from behind"></div>
  <div class="abs gallery-photo" style="left:550px;background:linear-gradient(135deg,#e8c88a,#f2d9a0 50%,#d8b070)" role="img" aria-label="Woman at a typewriter surrounded by crumpled paper"></div>
</main>

<footer>
  <div class="abs footer"></div>
  <div class="abs footer-links">Home<span>|</span>About Me<span>|</span>Publishes<span>|</span>In Media<span>|</span>Blog<span>|</span>Contact Me</div>
  <div class="abs copyright">Copyright © 2014 &nbsp;Mark Ellison. &nbsp;All rights reserved.</div>
  <span class="abs social" style="left:612px"></span>
  <span class="abs social" style="left:634px"></span>
  <span class="abs social" style="left:657px"></span>
  <span class="abs social" style="left:678px"></span>
</footer>

</body>
</html>
```